"Made in Chicago" Baby Shower Invitation

I need a design for a baby shower invitation with the headline and theme of "Made in Chicago". The design should incorporate the colors/design of the Chicago flag. I have attached an image of the flag for your reference. The design should be sized 5-1/2 wide x 8-1/2 long. I want to be able to print two to a page on a standard 8-1/2 X 11" piece of (nice quality) paper on a standard home printer.
Copy:
Made in Chicago Baby Shower
For: Mirela & Gordon
Date: Saturday, April 5, 2014
Time: 7:00 p.m.
Place: 42 West Halloway Ave, 5B
RSVP by April 1 to Dana Whitmoor/312-555-0193

Hello Designers - I corrected the size requirements of the invitation (bad math before) and added a few more notes of preference. Looking for a design that is more clean and graphic and less traditional, soft baby shower look. Thank you!

Friends & family of the 20-sometthing, urban professional couple who are having a baby.

Baby

Must have
• Chicago flag colors and/or image, the words "made in Chicago", and the (revised) size indicated.
Should not have
• Anything inappropriate or offensive to grandmother of said couple.

```html
<!DOCTYPE html>
<html lang="en">
<head>
<meta charset="utf-8">
<title>Made in Chicago Baby Shower Invitation</title>
<link rel="stylesheet" href="https://fonts.googleapis.com/css2?family=Cinzel:wght@400;500&family=Cormorant+Garamond:ital,wght@1,500;1,700&family=Chewy&display=swap">
<style>
  :root {
    --sky: #cdeaf8;
    --sky-deep: #bfe3f5;
    --flag-red: #e8141c;
    --label-red: #e2566c;
    --outline-blue: #9fd3ee;
    --rsvp-blue: #a9d8f0;
    --white: #ffffff;
  }
  * { margin: 0; padding: 0; box-sizing: border-box; }
  html, body { width: 1200px; height: 2400px; overflow: hidden; background: var(--white); }
  .invitation {
    position: relative;
    width: 1200px;
    height: 2400px;
    border: 8px solid var(--white);
    overflow: hidden;
  }
  .star-field {
    position: absolute;
    inset: 0;
    background: radial-gradient(ellipse at 50% 45%, var(--sky) 0%, var(--sky) 60%, var(--sky-deep) 100%);
  }
  .line { position: absolute; left: 0; width: 100%; text-align: center; white-space: nowrap; }
  .headline-caps {
    font-family: "Cinzel", serif;
    font-weight: 400;
    color: var(--flag-red);
    font-size: 150px;
    line-height: 1;
  }
  .headline-made { top: 55px; }
  .headline-in { top: 245px; }
  .headline-city {
    top: 420px;
    font-family: "Cormorant Garamond", serif;
    font-style: italic;
    font-weight: 700;
    font-size: 250px;
    line-height: 1;
    color: var(--flag-red);
    letter-spacing: -4px;
  }
  .event-title {
    font-family: "Chewy", cursive;
    font-size: 230px;
    line-height: 1;
    color: var(--white);
    -webkit-text-stroke: 8px var(--outline-blue);
    paint-order: stroke fill;
    letter-spacing: 4px;
  }
  .event-baby { top: 765px; }
  .event-shower { top: 965px; }
  .detail-label {
    position: absolute;
    left: 72px;
    font-family: "Chewy", cursive;
    font-size: 108px;
    line-height: 1;
    color: var(--label-red);
    -webkit-text-stroke: 6px var(--white);
    paint-order: stroke fill;
    text-shadow: 0 0 6px var(--outline-blue);
  }
  .detail-value {
    position: absolute;
    right: 72px;
    font-family: "Cinzel", serif;
    font-size: 50px;
    line-height: 1;
    color: var(--flag-red);
    white-space: nowrap;
  }
  .label-for { top: 1285px; }   .value-for { top: 1318px; }
  .label-date { top: 1400px; }  .value-date { top: 1432px; }
  .label-time { top: 1512px; }  .value-time { top: 1546px; }
  .label-place { top: 1625px; } .value-place { top: 1660px; font-size: 44px; right: 60px; }
  .rsvp {
    font-family: "Cormorant Garamond", serif;
    font-style: italic;
    font-weight: 500;
    font-size: 98px;
    line-height: 1;
    color: var(--rsvp-blue);
    text-shadow: 0 0 4px var(--white), 0 0 10px var(--white);
  }
  .rsvp-deadline { top: 1868px; }
  .rsvp-contact { top: 2030px; }
</style>
</head>
<body>
  <main class="invitation">
    <div class="star-field" role="img" aria-label="Light blue background scattered with small red and white stars"></div>

    <h1>
      <span class="line headline-caps headline-made">Made</span>
      <span class="line headline-caps headline-in">In</span>
      <span class="line headline-city">Chicago</span>
    </h1>

    <h2>
      <span class="line event-title event-baby">Baby</span>
      <span class="line event-title event-shower">Shower</span>
    </h2>

    <section class="details">
      <span class="detail-label label-for">for:</span>
      <span class="detail-value value-for">Mirela &amp; Gordon</span>
      <span class="detail-label label-date">date:</span>
      <span class="detail-value value-date">Saturday, April 5, 2014</span>
      <span class="detail-label label-time">time:</span>
      <span class="detail-value value-time">7.00 PM</span>
      <span class="detail-label label-place">place:</span>
      <span class="detail-value value-place">42 West Halloway Ave, 5B</span>
    </section>

    <footer>
      <p class="line rsvp rsvp-deadline">RSVP by April 1 to</p>
      <p class="line rsvp rsvp-contact">Dana Whitmoor/312-555-0193</p>
    </footer>
  </main>
</body>
</html>
```